Vertical flyer design to guide people to my shop

We need a vertical flyer design for a tailor shop, Marlow Stitchworks. Our shop is on the 3/F, and we need this flyer/poster to placed on the G/F street level to guide people to take the lifts upstairs. Basically to tell people that, "We are here on 3/F!"

Dimensions ratio: 80 (wide) x200 (tall)

You may use the photos and graphics from the webpages below.
http://www.marlowstitchworks.net/en/marlow-stitchworks-hong-kong-tailors-tailor-shop/

https://www.cloth-q.com/tailor/marlow-stitchworks

```html
<!DOCTYPE html>
<html lang="en">
<head>
<meta charset="utf-8">
<title>Marlow Stitchworks – We Are Here on 3/F</title>
<link rel="stylesheet" href="https://fonts.googleapis.com/css2?family=Jost:wght@300&family=Roboto:wght@400&family=Tinos:wght@400;700&display=swap">
<style>
  :root {
    --page-bg: #9e9798;
    --ink: #111111;
    --band-black: #060606;
    --band-grey: #8a8a8a;
    --panel-light: #f6f6f6;
    --panel-shade: #d9d9d9;
    --photo-dark: #0d0c0b;
    --photo-mid: #3a342e;
    --photo-warm: #7a6c5c;
    --white: #ffffff;
  }
  * { margin: 0; padding: 0; box-sizing: border-box; }
  html, body {
    width: 691px;
    height: 1200px;
    overflow: hidden;
    background: var(--page-bg);
  }
  .banner {
    position: absolute;
    left: 141px;
    top: 53px;
    width: 409px;
    height: 1094px;
  }
  .banner-shapes {
    position: absolute;
    inset: 0;
    width: 409px;
    height: 1094px;
    display: block;
  }
  .brand {
    position: absolute;
    top: 46px;
    left: 0;
    width: 100%;
    text-align: center;
    color: var(--white);
    font-family: "Tinos", "Times New Roman", serif;
  }
  .brand-name {
    font-weight: 700;
    font-size: 29px;
    line-height: 36px;
    letter-spacing: 0.5px;
  }
  .brand-tagline {
    margin-top: 10px;
    font-weight: 400;
    font-size: 14px;
    line-height: 24px;
  }
  .wayfinding {
    position: absolute;
    top: 680px;
    left: 0;
    width: 100%;
    text-align: center;
    color: var(--ink);
    font-family: "Jost", "Futura", sans-serif;
    font-weight: 300;
  }
  .wayfinding-lead {
    font-size: 60px;
    line-height: 72px;
    letter-spacing: -0.5px;
  }
  .wayfinding-floor {
    font-size: 90px;
    line-height: 90px;
    letter-spacing: 1px;
  }
  .wayfinding-hint {
    font-size: 32px;
    line-height: 44px;
    margin-top: 6px;
  }
  .web-address {
    position: absolute;
    top: 1050px;
    left: 0;
    width: 100%;
    text-align: center;
    color: var(--white);
    font-family: "Roboto", "Arial", sans-serif;
    font-size: 22px;
    line-height: 30px;
  }
</style>
</head>
<body>
  <main class="banner">
    <svg class="banner-shapes" viewBox="0 0 409 1094" aria-hidden="false">
      <defs>
        <linearGradient id="photoTone" x1="0" y1="0" x2="1" y2="1">
          <stop offset="0" stop-color="var(--photo-dark)"/>
          <stop offset="0.45" stop-color="var(--photo-mid)"/>
          <stop offset="0.7" stop-color="var(--photo-warm)"/>
          <stop offset="1" stop-color="var(--photo-dark)"/>
        </linearGradient>
        <radialGradient id="panelTone" cx="0.5" cy="0.55" r="0.75">
          <stop offset="0" stop-color="var(--panel-light)"/>
          <stop offset="1" stop-color="var(--panel-shade)"/>
        </radialGradient>
      </defs>
      <rect class="garment-photo" x="0" y="0" width="409" height="570" fill="url(#photoTone)" role="img" aria-label="Photo of tailored jackets hanging on a rail, a tweed jacket in front"/>
      <polygon class="panel-edge" points="0,516 409,556 409,570 0,528" fill="var(--band-grey)" opacity="0.55"/>
      <polygon class="message-panel" points="0,524 409,566 409,1020 0,1004" fill="url(#panelTone)"/>
      <polygon class="footer-edge" points="0,1002 409,1016 409,1030 0,1013" fill="var(--band-grey)"/>
      <polygon class="footer-band" points="0,1012 409,1028 409,1094 0,1094" fill="var(--band-black)"/>
    </svg>

    <header class="brand">
      <div class="brand-name">MARLOW<br>STITCHWORKS</div>
      <div class="brand-tagline">EXPERT LADIES’<br>&amp; GENT’S TAILORS</div>
    </header>

    <section class="wayfinding">
      <div class="wayfinding-lead">WE ARE HERE</div>
      <div class="wayfinding-floor">ON 3/F!</div>
      <div class="wayfinding-hint">take the lifts upstairs</div>
    </section>

    <footer class="web-address">www.marlowstitchworks.net</footer>
  </main>
</body>
</html>
```